Brackwater Vale Medical Website to make connecting and communicating easier

To create a unique, user-friendly, professional website for patients and professionals to access education/ information, forms, appointments, contact details, and data about us, and for us to have the capacity to link to various cloud-based platforms.
To use the logo design and colour scheme we have just sourced.

WEBSITE to be eye catching, Inspiring and alluring
- efficient and logical
- professional and trustworthy appearance
- health focus "living health matters"
- user friendly
- ability to link with cloud-based software and video conferencing tools/ telehealth
- colours- black/ white teal and ?silver

PAGES:
page 1 - Our clinic and staff, services offered, contact us- address/ map / contact details- social media connections
page 2- patients and visitors - New patient forms to complete, news and patient informtion (educatinal)
page 3 - health professionals -referral forms, research and education
page 3- online appointments
page 4 - Quick links - partners, other services
page 5- privacy policy, disclaimer

Need extra days to review

HI, Could we please extend the deadline another 5 days, so sorry just struggling with my workload to be able to keep up and I am wanting to liaise more with the designer that I will choose. I am so happy with PixelForge and all the designers - thank you! Thank you so much!!

Target Market(s)

Patients - mostly over 60's so the website must be minimal clicks and simple to navigate
Professionals - for education and access forms

Industry/Entity Type

Health Care

Coding

Coded - Design and coding required

Number of Pages Required

5+ page

Font styles to use
Sans Serif
Script

Colors
33b8a4
86cfc6

Requirements
Must have
• WEBSITE to be eye catching, Inspiring and alluring
- efficient and logical
- user friendly

WEBSITE - professional and user friendly
- ability to link with cloud based software and videoconferencing/ telehealth
Nice to have
• clean and crisp presentation
happy for an innovative look
room to add more services and ability to link pages and resources
Should not have
• Please ensure the website is not:
clunky
difficult to navigate
common and cheap looking

```html
<!DOCTYPE html>
<html lang="en">
<head>
<meta charset="utf-8">
<title>Brackwater Vale Medical</title>
<link href="https://fonts.googleapis.com/css2?family=Montserrat:wght@400;500;600;700&display=swap" rel="stylesheet">
<style>
:root{
  --teal:#36b7a3;
  --teal-light:#86cfc6;
  --teal-dark:#0f5f6b;
  --cyan:#1dbfcc;
  --ink:#1b1b1b;
  --text:#3a3a3a;
  --muted:#555;
  --mist:#f4fbfa;
  --line:#cfe9e5;
  --foot:#f1f1f1;
}
*{box-sizing:border-box;margin:0;padding:0}
html,body{width:1200px;height:3604px;overflow:hidden}
body{position:relative;font-family:'Montserrat',sans-serif;color:var(--text);background:#fff}
.abs{position:absolute}
svg{display:block}

/* top bar */
.topbar{left:0;top:0;width:1200px;height:31px;border-bottom:1px solid #eee}
.social{left:62px;top:10px;display:flex;gap:9px}
.social span{width:10px;height:10px;border-radius:50%;background:#222;display:block}
.address{left:474px;top:8px;font-size:12px;color:#333;display:flex;gap:6px;align-items:center;white-space:nowrap}
.top-phone{left:806px;top:0;width:146px;height:31px;background:var(--cyan);color:#fff;font-weight:600;font-size:14px;display:flex;align-items:center;justify-content:center;gap:6px;white-space:nowrap}
.top-book{left:952px;top:0;width:173px;height:31px;background:var(--teal-dark);color:#fff;font-weight:600;font-size:11px;display:flex;align-items:center;justify-content:center;gap:7px;letter-spacing:.3px;white-space:nowrap}

/* header */
.brand{left:70px;top:52px;display:flex;align-items:center;gap:8px;color:var(--teal);font-weight:700;font-size:15px;line-height:1.1;width:170px}
.brand i{width:26px;height:26px;background:var(--teal);flex:none}
.nav{left:323px;top:71px;display:flex;height:47px;font-size:14px;color:#333;white-space:nowrap}
.nav a{display:flex;align-items:center;padding:0 19px;color:inherit;text-decoration:none}
.nav a.active{background:var(--teal);color:#fff;font-weight:600;width:90px;justify-content:center;padding:0}

/* hero */
.hero{left:0;top:118px;width:1200px;height:487px;background:var(--teal)}
.hero h1{left:75px;top:114px;width:500px;color:#fff;font-size:29px;font-weight:600;letter-spacing:.2px;white-space:nowrap;z-index:2}
.hero .lead{left:75px;top:168px;color:#fff;font-size:17.5px;font-weight:600;line-height:1.45}
.hero .note{left:75px;top:224px;color:#e8f7f4;font-size:11px;white-space:nowrap}
.hero .phone{left:75px;top:265px;color:#fff;font-size:24px;font-weight:600;display:flex;gap:10px;align-items:center}
.btn-dark{background:var(--teal-dark);color:#fff;font-weight:600;display:flex;align-items:center;justify-content:center;gap:9px;letter-spacing:.3px;white-space:nowrap}
.hero .book{left:75px;top:315px;width:183px;height:46px;font-size:17px}
.hero .photo{left:595px;top:33px;width:575px;height:369px;background:linear-gradient(100deg,#1f9fbd 0%,#4fb3cf 45%,#cfdde3 75%,#eef2f4 100%)}
.dots{left:557px;top:444px;display:flex;gap:18px}
.dots span{width:16px;height:16px;border-radius:50%;border:2px solid #fff;position:relative}
.dots span::after{content:"";position:absolute;left:3px;top:3px;width:6px;height:6px;border-radius:50%;background:#fff}
.dots span.on{background:#fff}

/* welcome */
.welcome{left:0;top:605px;width:1200px;height:809px;background:var(--mist)}
.section-title{width:1200px;text-align:center;color:var(--ink);font-weight:600;font-size:32px}
.welcome .section-title{top:43px}
.intro{left:300px;width:600px;text-align:center;font-size:13.3px;line-height:1.42;color:#333}
.welcome .intro{top:100px}
.team-title{left:84px;top:248px;font-size:18px;font-weight:600;color:var(--ink)}
.team-text{left:84px;top:289px;width:265px;font-size:13.3px;line-height:1.4;color:#333}
.team-btn{left:84px;top:375px;width:178px;height:38px;font-size:12px}
.doc{width:175px}
.doc .ph{width:175px;height:187px;background:linear-gradient(180deg,#e9edf0,#c9d3da)}
.doc h4{font-size:10.5px;font-weight:700;color:#222;margin-top:15px}
.doc p{font-size:10px;color:#444;margin-top:8px;line-height:1.4}

/* services */
.services .section-title{top:1452px}
.services .intro{top:1504px;width:560px;left:320px}
.offering{top:1576px;width:1200px;text-align:center;font-size:13.3px;color:#333}
.svc{width:338px;height:94px;border:1.5px solid var(--line);background:#f7fcfb;display:flex;align-items:center}
.svc .tick{width:26px;height:26px;background:var(--teal);margin-left:22px;flex:none;display:flex;align-items:center;justify-content:center}
.svc .name{flex:1;font-size:15.5px;font-weight:600;color:#222;padding-left:16px;line-height:1.25}
.svc .go{width:58px;height:94px;background:var(--teal);flex:none;display:flex;align-items:center;justify-content:center;margin-right:-1.5px}

/* telehealth */
.tele{left:71px;top:2015px;width:1059px;height:378px;border:1.5px solid var(--line);background:#fff}
.tele h2{left:38px;top:26px;font-size:30px;font-weight:600;color:var(--ink)}
.tele .copy{left:38px;top:86px;width:368px;font-size:13.3px;line-height:1.42;color:#333}
.tele .copy p+p{margin-top:14px}
.tele .book{left:40px;top:300px;width:183px;height:47px;font-size:17px}
.tele .photo{left:435px;top:-1.5px;width:625px;height:378px;background:linear-gradient(120deg,#c9bfae 0%,#8f9a78 40%,#d9cfc4 70%,#b7b9c4 100%)}

/* new patient */
.newpat{left:71px;top:2418px;width:1059px;height:154px;background:var(--teal)}
.newpat .photo{left:0;top:0;width:504px;height:154px;background:linear-gradient(110deg,#4a4a4a 0%,#e8e6e4 35%,#f4f2f0 70%,#d6c6c0 100%)}
.newpat h2{left:580px;top:30px;color:#fff;font-size:26px;font-weight:600}
.newpat .dl{left:580px;top:87px;width:311px;height:36px;font-size:12px}

/* news */
.news .section-title{top:2628px}
.card{width:322px}
.card .ph{width:322px;height:234px;position:relative}
.card .tag{position:absolute;right:0;bottom:0;width:146px;height:39px;background:var(--teal);color:#fff;font-size:11.5px;font-weight:600;display:flex;align-items:center;justify-content:center;letter-spacing:.3px}
.card h3{font-size:18px;font-weight:600;color:#222;line-height:1.25;margin-top:22px;padding-left:2px}
.card .more{width:124px;height:36px;font-size:12.5px;margin-top:22px}

/* footer */
.footer{left:0;top:3133px;width:1200px;height:429px;background:var(--foot)}
.fcol{font-size:11.5px;color:#333;line-height:22px}
.fcol h5{color:var(--teal);font-size:13px;font-weight:600;margin-bottom:4px;letter-spacing:.2px;white-space:nowrap}
.fcol b{font-weight:700;color:#222}
.f-phone{width:173px;height:33px;background:var(--cyan);color:#fff;font-weight:600;font-size:15px;display:flex;align-items:center;justify-content:center;gap:7px}
.f-book{width:173px;height:33px;font-size:12px}
.bottom{left:0;top:3562px;width:1200px;height:42px;background:var(--teal)}
.bottom .copy{left:127px;top:15px;font-size:10px;color:#fff}
.bottom .social{left:1010px;top:16px}
.bottom .social span{background:#fff}
</style>
</head>
<body>

<div class="abs topbar"></div>
<div class="abs social" aria-label="Social links"><span></span><span></span><span></span></div>
<div class="abs address">
  <svg width="11" height="15" viewBox="0 0 11 15"><path d="M5.5 0C2.5 0 0 2.4 0 5.4 0 9.3 5.5 15 5.5 15S11 9.3 11 5.4C11 2.4 8.5 0 5.5 0zm0 7.6a2.2 2.2 0 1 1 0-4.4 2.2 2.2 0 0 1 0 4.4z" fill="#222"/></svg>
  48 Harbour Lane, Brackwater NSW 2100 Australia
</div>
<div class="abs top-phone">
  <svg width="14" height="14" viewBox="0 0 24 24"><path d="M6.6 10.8a15 15 0 0 0 6.6 6.6l2.2-2.2c.3-.3.7-.4 1-.2 1.1.4 2.3.6 3.6.6.6 0 1 .4 1 1V20c0 .6-.4 1-1 1A17 17 0 0 1 3 4c0-.6.4-1 1-1h3.5c.6 0 1 .4 1 1 0 1.3.2 2.5.6 3.6.1.3 0 .7-.2 1z" fill="none" stroke="#fff" stroke-width="2"/></svg>
  02 9555 0142
</div>
<div class="abs top-book">
  <svg width="13" height="13" viewBox="0 0 14 14"><rect x="1" y="2" width="12" height="11" fill="#fff"/><rect x="3" y="6" width="2" height="2" fill="#0f5f6b"/><rect x="6" y="6" width="2" height="2" fill="#0f5f6b"/><rect x="9" y="6" width="2" height="2" fill="#0f5f6b"/><rect x="3" y="9" width="2" height="2" fill="#0f5f6b"/><rect x="6" y="9" width="2" height="2" fill="#0f5f6b"/></svg>
  BOOK APPOINTMENT
</div>

<div class="abs brand"><i></i><span>Brackwater Vale Medical</span></div>
<nav class="abs nav">
  <a class="active">Home</a><a>Our Clinic &amp; Staff</a><a>Services</a><a>Patients &amp; Visitors</a><a>Health Professionals</a><a>News</a><a>Contact</a>
</nav>

<section class="abs hero">
  <div class="abs photo" role="img" aria-label="Doctor in blue scrubs with stethoscope holding a tablet in a hospital corridor"></div>
  <h1 class="abs">BRACKWATER VALE MEDICAL</h1>
  <div class="abs lead">Bulk Billed Telehealth Appointments<br>Now Available*</div>
  <div class="abs note">*Patients must hold a Valid Medicare or DVA card. Participating GPs Only.</div>
  <div class="abs phone">
    <svg width="20" height="20" viewBox="0 0 24 24"><path d="M6.6 10.8a15 15 0 0 0 6.6 6.6l2.2-2.2c.3-.3.7-.4 1-.2 1.1.4 2.3.6 3.6.6.6 0 1 .4 1 1V20c0 .6-.4 1-1 1A17 17 0 0 1 3 4c0-.6.4-1 1-1h3.5c.6 0 1 .4 1 1 0 1.3.2 2.5.6 3.6.1.3 0 .7-.2 1z" fill="none" stroke="#fff" stroke-width="1.8"/></svg>
    02 9555 0142
  </div>
  <div class="abs btn-dark book">
    <svg width="16" height="16" viewBox="0 0 14 14"><rect x="1" y="2" width="12" height="11" fill="#fff"/><rect x="3" y="6" width="2" height="2" fill="#0f5f6b"/><rect x="6" y="6" width="2" height="2" fill="#0f5f6b"/><rect x="9" y="6" width="2" height="2" fill="#0f5f6b"/><rect x="3" y="9" width="2" height="2" fill="#0f5f6b"/><rect x="6" y="9" width="2" height="2" fill="#0f5f6b"/></svg>
    BOOK ONLINE
  </div>
  <div class="abs dots"><span class="on"></span><span></span><span></span></div>
</section>

<section class="abs welcome">
  <h2 class="abs section-title">Welcome to Brackwater Vale Medical</h2>
  <p class="abs intro">Welcome to Brackwater Vale Medical, family friendly bulk billing GP Clinic. Conveniently located in Harbour Medical Centre, opposite the Brackwater Children's Hospital. Our GP Clinic offers a wide variety of services to help you and your family with all your health and wellbeing needs.</p>
  <h3 class="abs team-title">Our Team</h3>
  <p class="abs team-text">Meet the Brackwater Vale Medical team of diverse doctors who specialise in all aspects of your health care.</p>
  <div class="abs btn-dark team-btn">OUR CLINIC &amp; STAFF</div>

  <div class="abs doc" style="left:445px;top:238px"><div class="ph" role="img" aria-label="Portrait of a male doctor in white coat"></div><h4>DR MARTIN HALE</h4><p>MBBS, FRACGP<br>Clinical Director</p></div>
  <div class="abs doc" style="left:658px;top:238px"><div class="ph" role="img" aria-label="Portrait of a female doctor in blue scrubs"></div><h4>DR ANIKA RAO</h4><p>FRACGP, Diplomat ABFM</p></div>
  <div class="abs doc" style="left:871px;top:238px"><div class="ph" role="img" aria-label="Portrait of a female doctor in light blazer"></div><h4>DR HELEN MARSH</h4><p>MD, FRACGP</p></div>
  <div class="abs doc" style="left:445px;top:522px"><div class="ph" role="img" aria-label="Portrait of a male doctor with glasses"></div><h4>DR KENJI OTA</h4><p>MD, FRACGP</p></div>
  <div class="abs doc" style="left:658px;top:522px"><div class="ph" role="img" aria-label="Portrait of a smiling female doctor"></div><h4>DR LUCIA FERRO</h4><p>MD, FRACGP</p></div>
  <div class="abs doc" style="left:871px;top:522px"><div class="ph" role="img" aria-label="Portrait of a male doctor in white coat"></div><h4>DR PETER VANCE</h4><p>MD, FRACGP</p></div>
</section>

<section class="services">
  <h2 class="abs section-title">Services We Offer</h2>
  <p class="abs intro">At Brackwater Vale Medical, we strive to provide professional, reliable advice and treatment for the Community . We believe in providing quality health care in a safe and friendly environment.</p>
  <p class="abs offering">Offering a wide range of patient services:</p>

  <div class="abs svc" style="left:71px;top:1630px"><div class="tick"><svg width="16" height="12" viewBox="0 0 16 12"><path d="M1.5 6l4.5 4.5L14.5 1.5" fill="none" stroke="#fff" stroke-width="2.2"/></svg></div><div class="name">General Practitioner<br>Services</div><div class="go"><svg width="16" height="14" viewBox="0 0 16 14"><path d="M1 7h13M8.5 1.5L14 7l-5.5 5.5" fill="none" stroke="#fff" stroke-width="1.8"/></svg></div></div>
  <div class="abs svc" style="left:430px;top:1630px"><div class="tick"><svg width="16" height="12" viewBox="0 0 16 12"><path d="M1.5 6l4.5 4.5L14.5 1.5" fill="none" stroke="#fff" stroke-width="2.2"/></svg></div><div class="name">Allied Health</div><div class="go"><svg width="16" height="14" viewBox="0 0 16 14"><path d="M1 7h13M8.5 1.5L14 7l-5.5 5.5" fill="none" stroke="#fff" stroke-width="1.8"/></svg></div></div>
  <div class="abs svc" style="left:792px;top:1630px"><div class="tick"><svg width="16" height="12" viewBox="0 0 16 12"><path d="M1.5 6l4.5 4.5L14.5 1.5" fill="none" stroke="#fff" stroke-width="2.2"/></svg></div><div class="name">Women's Health<br>Checks</div><div class="go"><svg width="16" height="14" viewBox="0 0 16 14"><path d="M1 7h13M8.5 1.5L14 7l-5.5 5.5" fill="none" stroke="#fff" stroke-width="1.8"/></svg></div></div>

  <div class="abs svc" style="left:71px;top:1744px"><div class="tick"><svg width="16" height="12" viewBox="0 0 16 12"><path d="M1.5 6l4.5 4.5L14.5 1.5" fill="none" stroke="#fff" stroke-width="2.2"/></svg></div><div class="name">Men's Health Checks</div><div class="go"><svg width="16" height="14" viewBox="0 0 16 14"><path d="M1 7h13M8.5 1.5L14 7l-5.5 5.5" fill="none" stroke="#fff" stroke-width="1.8"/></svg></div></div>
  <div class="abs svc" style="left:430px;top:1744px"><div class="tick"><svg width="16" height="12" viewBox="0 0 16 12"><path d="M1.5 6l4.5 4.5L14.5 1.5" fill="none" stroke="#fff" stroke-width="2.2"/></svg></div><div class="name">Children's Health<br>Checks</div><div class="go"><svg width="16" height="14" viewBox="0 0 16 14"><path d="M1 7h13M8.5 1.5L14 7l-5.5 5.5" fill="none" stroke="#fff" stroke-width="1.8"/></svg></div></div>
  <div class="abs svc" style="left:792px;top:1744px"><div class="tick"><svg width="16" height="12" viewBox="0 0 16 12"><path d="M1.5 6l4.5 4.5L14.5 1.5" fill="none" stroke="#fff" stroke-width="2.2"/></svg></div><div class="name">Minor Operations</div><div class="go"><svg width="16" height="14" viewBox="0 0 16 14"><path d="M1 7h13M8.5 1.5L14 7l-5.5 5.5" fill="none" stroke="#fff" stroke-width="1.8"/></svg></div></div>

  <div class="abs svc" style="left:71px;top:1852px"><div class="tick"><svg width="16" height="12" viewBox="0 0 16 12"><path d="M1.5 6l4.5 4.5L14.5 1.5" fill="none" stroke="#fff" stroke-width="2.2"/></svg></div><div class="name">Chronic Disease<br>Management Plans</div><div class="go"><svg width="16" height="14" viewBox="0 0 16 14"><path d="M1 7h13M8.5 1.5L14 7l-5.5 5.5" fill="none" stroke="#fff" stroke-width="1.8"/></svg></div></div>
  <div class="abs svc" style="left:430px;top:1852px"><div class="tick"><svg width="16" height="12" viewBox="0 0 16 12"><path d="M1.5 6l4.5 4.5L14.5 1.5" fill="none" stroke="#fff" stroke-width="2.2"/></svg></div><div class="name">Pathology</div><div class="go"><svg width="16" height="14" viewBox="0 0 16 14"><path d="M1 7h13M8.5 1.5L14 7l-5.5 5.5" fill="none" stroke="#fff" stroke-width="1.8"/></svg></div></div>
  <div class="abs svc" style="left:792px;top:1852px"><div class="tick"><svg width="16" height="12" viewBox="0 0 16 12"><path d="M1.5 6l4.5 4.5L14.5 1.5" fill="none" stroke="#fff" stroke-width="2.2"/></svg></div><div class="name">Bereavement</div><div class="go"><svg width="16" height="14" viewBox="0 0 16 14"><path d="M1 7h13M8.5 1.5L14 7l-5.5 5.5" fill="none" stroke="#fff" stroke-width="1.8"/></svg></div></div>
</section>

<section class="abs tele">
  <h2 class="abs">Telehealth</h2>
  <div class="abs copy">
    <p>At Brackwater Vale Medical we value your health and ask you to do the same. Do not neglect your general/ regular health needs. All our doctors are still available for consultations via phone, video conference or face to face.</p>
    <p>To prevent the spread of COVID-19 the Australian government has introduced Telehealth. Your doctor at Brackwater Vale Medical will consult with you in the usual manner via a bulk billed telephone or video link.</p>
  </div>
  <div class="abs btn-dark book">
    <svg width="16" height="16" viewBox="0 0 14 14"><rect x="1" y="2" width="12" height="11" fill="#fff"/><rect x="3" y="6" width="2" height="2" fill="#0f5f6b"/><rect x="6" y="6" width="2" height="2" fill="#0f5f6b"/><rect x="9" y="6" width="2" height="2" fill="#0f5f6b"/><rect x="3" y="9" width="2" height="2" fill="#0f5f6b"/><rect x="6" y="9" width="2" height="2" fill="#0f5f6b"/></svg>
    BOOK ONLINE
  </div>
  <div class="abs photo" role="img" aria-label="Smiling older woman on a sofa holding a tablet for a video consultation"></div>
</section>

<section class="abs newpat">
  <div class="abs photo" role="img" aria-label="Hand with a pen filling in a registration form"></div>
  <h2 class="abs">New Patient?</h2>
  <div class="abs btn-dark dl">DOWNLOAD OUR REGISTRATION FORMS</div>
</section>

<section class="news">
  <h2 class="abs section-title">Latest Clinic News</h2>
  <article class="abs card" style="left:83px;top:2703px">
    <div class="ph" role="img" aria-label="Older woman at a kitchen table on a video call with a doctor" style="background:linear-gradient(120deg,#5a5550,#a7a29c 55%,#d8d5d0)"><span class="tag">FAMILY HEALTH</span></div>
    <h3>Is your Heart Health at risk?</h3>
    <div class="btn-dark more">READ MORE</div>
  </article>
  <article class="abs card" style="left:440px;top:2703px">
    <div class="ph" role="img" aria-label="Physiotherapist applying tape to a patient's arm" style="background:linear-gradient(120deg,#d9867e,#f0b7ad 50%,#e89c94)"><span class="tag">GENERAL HEALTH</span></div>
    <h3>Physiotherapists will virtually track their patients' recovery</h3>
    <div class="btn-dark more">READ MORE</div>
  </article>
  <article class="abs card" style="left:797px;top:2703px">
    <div class="ph" role="img" aria-label="Pregnant woman in a yellow top in soft sunlight" style="background:linear-gradient(120deg,#f2ecd8,#d9c37a 50%,#b79a52)"><span class="tag">WOMEN'S HEALTH</span></div>
    <h3>Ask the doctor: Is pregnancy glow real?</h3>
    <div class="btn-dark more">READ MORE</div>
  </article>
</section>

<footer class="abs footer">
  <div class="abs fcol" style="left:127px;top:54px">
    <h5>OUR CLINIC &amp; STAFF</h5>
    Overview<br>Meet our Staff<br>Employment<br>Privacy Policy<br>Disclaimer
  </div>
  <div class="abs fcol" style="left:127px;top:222px">
    <h5>QUICK LINKS</h5>
    Flu Pandemic<br>Immunisation Schedule<br>Family GP<br>Health Info Online<br>My Doctor<br>Wellness Portal<br>and more....
  </div>
  <div class="abs fcol" style="left:325px;top:54px">
    <h5>SERVICES</h5>
    General Practice<br>Vasectomy Centre<br>Travel Health<br>Cosmetic Clinic<br>Treatment of acute illnesses<br>Disease prevention<br>Family Health<br>Immunisations<br>Sports Health<br>Women's Health<br>Shared Maternity Care<br>Aviation medicals<br>Medical Acupuncture<br>PRP Therapy<br>Botox
  </div>
  <div class="abs fcol" style="left:524px;top:54px;width:190px">
    <h5>HEALTH PROFESSIONALS</h5>
    GP liaison<br>Clinical education<br>Referral templates &amp; criteria<br>
    <div style="line-height:15px;margin-top:4px;width:175px">GP Continuing Professional Development</div>
  </div>
  <div class="abs fcol" style="left:749px;top:54px">
    <h5>HOURS &amp; FEES</h5>
    <b>Monday to Friday:</b><br>8:00am – 11:00pm<br>
    <div style="margin-top:6px"><b>Saturday &amp; Sunday:</b><br>9:00am – 5:00pm</div>
    <div style="margin-top:20px"><b>Fees &amp; Billing</b></div>
  </div>
  <div class="abs fcol" style="left:924px;top:54px;line-height:15px">
    <h5 style="margin-bottom:6px">CONTACT US</h5>
    48 Harbour Lane<br>Brackwater NSW 2100, Australia
    <div style="margin-top:10px"><b>We are open 7 Days</b><br>Contact Us today to arrange<br>a GP appointment on:</div>
  </div>
  <div class="abs f-phone" style="left:922px;top:200px">
    <svg width="14" height="14" viewBox="0 0 24 24"><path d="M6.6 10.8a15 15 0 0 0 6.6 6.6l2.2-2.2c.3-.3.7-.4 1-.2 1.1.4 2.3.6 3.6.6.6 0 1 .4 1 1V20c0 .6-.4 1-1 1A17 17 0 0 1 3 4c0-.6.4-1 1-1h3.5c.6 0 1 .4 1 1 0 1.3.2 2.5.6 3.6.1.3 0 .7-.2 1z" fill="none" stroke="#fff" stroke-width="2"/></svg>
    02 9555 0142
  </div>
  <div class="abs btn-dark f-book" style="left:922px;top:245px">
    <svg width="13" height="13" viewBox="0 0 14 14"><rect x="1" y="2" width="12" height="11" fill="#fff"/><rect x="3" y="6" width="2" height="2" fill="#0f5f6b"/><rect x="6" y="6" width="2" height="2" fill="#0f5f6b"/><rect x="9" y="6" width="2" height="2" fill="#0f5f6b"/><rect x="3" y="9" width="2" height="2" fill="#0f5f6b"/><rect x="6" y="9" width="2" height="2" fill="#0f5f6b"/></svg>
    BOOK APPOINTMENT
  </div>
</footer>
<div class="abs bottom">
  <div class="abs copy">© 2020 Brackwater Vale Medical. All rights reserved.</div>
  <div class="abs social" aria-label="Social links"><span></span><span></span><span></span></div>
</div>

</body>
</html>
```